** Wanted ** Wordpress web design for scaffolding rental and construction company

We need a website design and must be functional to show a basic overview of what our company offers as a service. We have a domain name and a logo but we need web design. This web site should have another scaffolding rental page for construction and renovation as well as a quote section where customers can enter their personal information and also upload photos. The site% 26quot; www.corvithane.com% 26quot; should be intuitive, clear and classy ... The logo must be found on the site in several ways.

Target Market(s)

Professional and no professional

Coding

Coded - Design and coding required

Number of Pages Required

3 page

Font styles to use
Serif
Sans Serif
Decorative
Script

Requirements
Must have
• Our logo
Nice to have
• Slogan:% 26quot; The height% 26 # 224; port% 26 # 233; e hand% 26quot;

```html
<!DOCTYPE html>
<html lang="en">
<head>
<meta charset="utf-8">
<title>Corvithane — Scaffolding Rental and Construction Company</title>
<link href="https://fonts.googleapis.com/css2?family=Open+Sans:ital,wght@0,400;0,600;0,700;1,600&family=Oswald:wght@500&display=swap" rel="stylesheet">
<style>
:root{
  --orange:#f15a22;
  --orange-soft:#fbe3d8;
  --ink:#333;
  --muted:#8a8a8a;
  --light:#f3f3f3;
  --dark:#1f2028;
  --darker:#16171d;
  --field:#2e3039;
  --white:#fff;
}
*{box-sizing:border-box;margin:0;padding:0}
html,body{width:1200px;height:4013px;overflow:hidden}
body{position:relative;font-family:'Open Sans',sans-serif;color:var(--ink);background:var(--white)}
.abs{position:absolute}
.accent{color:var(--orange)}
.section-title{position:absolute;left:0;width:1200px;text-align:center;font-size:26px;font-weight:400;text-transform:uppercase;letter-spacing:.5px}
.section-title::after{content:"";display:block;width:130px;height:2px;background:var(--orange);margin:10px auto 0}
.btn{position:absolute;background:var(--orange);color:var(--white);font-size:11px;font-weight:600;text-transform:uppercase;display:flex;align-items:center;justify-content:center;letter-spacing:.3px}

/* nav */
.nav{position:absolute;top:0;left:0;width:1200px;height:52px;background:var(--white);display:flex;align-items:center}
.nav-links{position:absolute;left:355px;top:0;height:52px;display:flex;gap:0}
.nav-links a{display:flex;align-items:center;padding:0 11px;font-size:11px;color:#333;text-decoration:none;text-transform:uppercase;height:52px}
.nav-links a.active{color:var(--orange);border-top:3px solid var(--orange);border-bottom:3px solid var(--orange);background:#fdf1ec}
.nav .btn{left:980px;top:8px;width:133px;height:36px}

/* hero */
.hero{position:absolute;top:52px;left:0;width:1200px;height:490px;background:linear-gradient(135deg,#3a2a1f 0%,#5a4a38 35%,#2a2622 70%,#453628 100%)}
.hero-shade{position:absolute;inset:0;background:rgba(0,0,0,.35)}
.brand{position:absolute;display:flex;align-items:center;justify-content:center;gap:12px;color:var(--orange);font-weight:700;letter-spacing:3px}
.brand .mark{background:var(--orange)}
.hero .brand{left:0;width:1200px;top:150px;font-size:34px}
.hero .brand .mark{width:22px;height:22px}
.hero-tag{position:absolute;top:250px;width:1200px;text-align:center;color:var(--white);font-family:'Oswald',sans-serif;font-size:25px;letter-spacing:2px}
.hero-call{position:absolute;top:290px;width:1200px;text-align:center;color:var(--white);font-size:25px}
.hero .btn{left:532px;top:341px;width:138px;height:38px}
.dots{position:absolute;top:436px;left:585px;display:flex;gap:5px;align-items:center}
.dots span{width:5px;height:5px;border-radius:50%;background:#ddd}
.dots span.on{width:8px;height:8px;border:2px solid #ddd;background:transparent}

/* quote */
.quote{position:absolute;top:542px;left:0;width:1200px;height:248px;background:var(--light);overflow:hidden}
.quote .deco{position:absolute;left:-30px;top:40px;width:190px;height:180px;background:var(--orange-soft);transform:rotate(-12deg)}
.quote .section-title{top:36px}
.field{position:absolute;height:46px;background:var(--white);border:1px solid #c9c9c9;font-size:16px;color:#666;display:flex;align-items:center;padding-left:12px}
.quote .btn{left:542px;top:175px;width:118px;height:36px;background:#4a4a4a}

/* about */
.about-text{position:absolute;top:790px;left:0;width:600px;height:315px;background:linear-gradient(135deg,#4a4a4a,#3b3b3b 60%,#555)}
.about-text h2{position:absolute;left:89px;top:65px;font-size:26px;font-weight:400;color:var(--white)}
.about-text h2::after{content:"";display:block;width:85px;height:2px;background:var(--orange);margin-top:8px}
.about-text p{position:absolute;left:89px;top:132px;width:450px;font-size:11px;line-height:16.5px;color:#e6e6e6}
.about-photo{position:absolute;top:790px;left:600px;width:600px;height:315px;background:linear-gradient(180deg,#3d6fc2 0%,#5b8fd8 45%,#6a5a48 100%)}

/* what we do */
.wwd-frame{position:absolute;left:125px;top:1181px;width:899px;height:485px;border:2px solid var(--orange)}
.wwd-photo{position:absolute;left:157px;top:1209px;width:655px;height:423px;background:linear-gradient(160deg,#c9d9e8 0%,#9fb3c4 40%,#6a4a32 100%)}
.card{position:absolute;background:var(--white);box-shadow:0 4px 18px rgba(0,0,0,.15);overflow:hidden}
.wwd-card{left:725px;top:1265px;width:352px;height:301px}
.card .deco{position:absolute;background:var(--orange-soft);opacity:.7}
.card h3{position:relative;font-size:25px;font-weight:400;text-transform:uppercase}
.card h3::after{content:"";display:block;width:45px;height:2px;background:var(--orange);margin-top:10px}
.card p{position:relative;font-size:11px;line-height:16px;color:#777}
.readmore{position:relative;font-size:8px;font-weight:700;color:#444;display:flex;align-items:center;gap:6px;text-transform:uppercase}
.readmore svg{display:block}

/* projects */
.projects{position:absolute;top:1749px;left:0;width:1200px;height:791px;background:linear-gradient(135deg,#1c1d22,#2b2a28 40%,#1a1b20 80%,#262522)}
.projects .section-title{color:var(--white);top:44px}
.tile{position:absolute;width:284px;height:227px;border:2px solid var(--white)}
.projects .btn{left:522px;top:679px;width:157px;height:47px;font-size:11px}

/* blog */
.blog-deco{position:absolute;left:860px;top:2640px;width:330px;height:355px;background:var(--orange-soft);opacity:.6;transform:rotate(-10deg)}
.blog-frame{position:absolute;left:391px;top:2599px;width:446px;height:314px;border:2px solid var(--orange)}
.blog-photo{position:absolute;left:520px;top:2624px;width:293px;height:261px;background:linear-gradient(180deg,#3f78c8 0%,#6a9ad8 55%,#8a5a3a 100%)}
.blog-card{left:360px;top:2660px;width:206px;height:184px;padding:26px 22px}
.blog-card h3{font-size:13px}
.blog-card h3::after{display:none}
.blog-card p{font-size:8px;line-height:10px;margin-top:12px;text-align:justify}
.blog-card .readmore{margin-top:14px;font-size:7px}
.pager{position:absolute;top:2938px;width:21px;height:20px;display:flex;align-items:center;justify-content:center}

/* testimonials */
.testimonials{position:absolute;top:2995px;left:0;width:1200px;height:536px;background:var(--light)}
.testimonials .section-title{top:52px}
.t-card{position:absolute;background:var(--white);text-align:center;padding:0 26px}
.t-card .q{color:var(--orange);font-size:26px;font-weight:700;font-family:Georgia,serif;margin-top:12px;height:20px}
.t-card .avatar{width:56px;height:56px;border-radius:50%;background:#c4c4c4;margin:0 auto}
.t-card p{font-size:11.5px;line-height:17px;color:#555;text-align:justify;margin-top:22px}
.t-card.faded{opacity:.45}
.t-card .name{text-align:left;color:var(--orange);font-style:italic;font-weight:600;font-size:11px;margin-top:20px}
.t-card .loc{text-align:left;font-size:7px;letter-spacing:2px;color:#666}

/* footer */
.footer{position:absolute;top:3531px;left:0;width:1200px;height:458px;background:var(--dark)}
.footer .divider{position:absolute;left:600px;top:50px;width:1px;height:380px;background:#454650}
.footer .brand{left:140px;width:400px;top:195px;font-size:28px}
.footer .brand .mark{width:20px;height:20px}
.f-tag{position:absolute;left:120px;width:460px;top:265px;text-align:center;color:var(--white);font-size:14.5px}
.f-call{position:absolute;left:120px;width:460px;top:293px;text-align:center;color:var(--white);font-size:19px}
.socials{position:absolute;left:272px;top:340px;display:flex;gap:16px}
.socials span{width:33px;height:33px;border:2px solid var(--white);border-radius:50%}
.footer h2{position:absolute;left:623px;top:102px;color:var(--white);font-size:25px;font-weight:600}
.f-field{position:absolute;background:var(--field);color:#8a8b93;font-size:8px;padding:10px}
.footer .btn{left:623px;top:336px;width:75px;height:28px;font-size:8px}
.copyright{position:absolute;top:3989px;left:0;width:1200px;height:24px;background:var(--darker);color:#888;font-size:8px;display:flex;align-items:center;justify-content:center}
</style>
</head>
<body>

<header class="nav">
  <nav class="nav-links">
    <a class="active" href="#">Home</a>
    <a href="#">About Us</a>
    <a href="#">Services</a>
    <a href="#">Projects</a>
    <a href="#">Gallery</a>
    <a href="#">Contact Us</a>
  </nav>
  <div class="btn">Request a Quote</div>
</header>

<section class="hero" role="img" aria-label="Workers in hard hats on scaffolding at a building site">
  <div class="hero-shade"></div>
  <div class="brand"><span class="mark"></span>CORVITHANE</div>
  <div class="hero-tag">SCAFFOLDING RENTAL AND CONSTRUCTION COMPANY</div>
  <div class="hero-call"><span class="accent">CALL US NOW :</span> 555 013 0000</div>
  <div class="btn">Learn More</div>
  <div class="dots"><span></span><span class="on"></span><span></span></div>
</section>

<section class="quote">
  <div class="deco"></div>
  <h2 class="section-title">Request a <span class="accent">Quote</span></h2>
  <div class="field" style="left:78px;top:106px;width:250px">Name</div>
  <div class="field" style="left:343px;top:106px;width:250px">Phone</div>
  <div class="field" style="left:610px;top:106px;width:250px">Email</div>
  <div class="field" style="left:877px;top:106px;width:251px">Service Type
    <svg class="abs" style="right:14px;top:18px" width="12" height="8" viewBox="0 0 12 8"><path d="M1 1l5 5 5-5" fill="none" stroke="#999" stroke-width="1.4"/></svg>
  </div>
  <div class="btn">Submit</div>
</section>

<section class="about-text" role="img" aria-label="Dark textured background">
  <h2>About <span class="accent">Us</span></h2>
  <p>Lorem Ipsum is simply dummy text of the printing and typesetting industry. Lorem Ipsum has been the industry's standard dummy text ever since the 1500s, when an unknown printer took a galley of type and scrambled it to make a type specimen book. It has survived not only five centuries, but also the leap into electronic typesetting, remaining essentially unchanged. It was popularised in the 1960s with the release of Letraset sheets containing Lorem Ipsum passages, and more recently with desktop publishing software like Aldus PageMaker including versions of Lorem Ipsum.</p>
</section>
<div class="about-photo" role="img" aria-label="Worker in a hard hat tying steel rebar against a blue sky"></div>

<div class="wwd-frame"></div>
<div class="wwd-photo" role="img" aria-label="Workers climbing steel rebar columns on a construction site"></div>
<article class="card wwd-card">
  <div class="deco" style="right:30px;top:40px;width:110px;height:200px"></div>
  <div style="position:relative;padding:50px 34px 0">
    <h3>What <span class="accent">We Do</span></h3>
    <p style="margin-top:24px">Lorem Ipsum is simply dummy text of the printing and typesetting industry. Lorem Ipsum has been the industry's standard dummy text ever since the 1500s, when an unknown printer took a galley of type and scrambled it to make a type specimen book</p>
    <div class="readmore" style="margin-top:22px">Read More <svg width="16" height="6" viewBox="0 0 16 6"><path d="M0 3h14M11 .5L14 3l-3 2.5" fill="none" stroke="#f15a22"/></svg></div>
  </div>
</article>

<section class="projects" role="img" aria-label="Dark background of building scaffolding">
  <h2 class="section-title">Resent <span class="accent">Projects</span></h2>
  <div class="tile" style="left:151px;top:132px;background:linear-gradient(135deg,#b9b9b9,#8a4a2a 60%,#e0e0e0)" role="img" aria-label="Orange formwork on a building under construction"></div>
  <div class="tile" style="left:457px;top:132px;background:linear-gradient(160deg,#1c3f8a,#c8ccd2 50%,#1d3b7a)" role="img" aria-label="White high-rise apartment tower"></div>
  <div class="tile" style="left:760px;top:132px;background:linear-gradient(180deg,#5a4a38,#8a7a60 50%,#6a6050)" role="img" aria-label="Long scaffolding corridor inside a building"></div>
  <div class="tile" style="left:151px;top:388px;background:linear-gradient(180deg,#c9d3dc,#7a8494 60%,#a89a88)" role="img" aria-label="Building wrapped in scaffolding"></div>
  <div class="tile" style="left:457px;top:388px;background:linear-gradient(135deg,#3a3a3a,#c79a2a 50%,#4a4a4a)" role="img" aria-label="Yellow scaffolding frames"></div>
  <div class="tile" style="left:760px;top:388px;background:linear-gradient(160deg,#d8d8d8,#6a6a6a 60%,#3a3a3a)" role="img" aria-label="Tall building covered in scaffolding, black and white"></div>
  <div class="btn">View More</div>
</section>

<div class="blog-deco"></div>
<div class="blog-frame"></div>
<div class="blog-photo" role="img" aria-label="Worker in safety harness climbing rebar against a blue sky"></div>
<article class="card blog-card">
  <h3>Lasest <span class="accent">Blog</span></h3>
  <p>Lorem Ipsum is simply dummy text of the printing and typesetting industry. Lorem Ipsum has been the industry's standard dummy text ever since the 1500s, when an unknown printer took a galley of type and scrambled it.</p>
  <div class="readmore">Read More <svg width="14" height="6" viewBox="0 0 14 6"><path d="M0 3h12M9 .5L12 3l-3 2.5" fill="none" stroke="#f15a22"/></svg></div>
</article>
<div class="pager" style="left:576px;background:#444"><svg width="6" height="9" viewBox="0 0 6 9"><path d="M5 1L1.5 4.5 5 8" fill="none" stroke="#fff" stroke-width="1.5"/></svg></div>
<div class="pager" style="left:603px;background:var(--orange)"><svg width="6" height="9" viewBox="0 0 6 9"><path d="M1 1l3.5 3.5L1 8" fill="none" stroke="#fff" stroke-width="1.5"/></svg></div>

<section class="testimonials">
  <h2 class="section-title">Our <span class="accent">Testimonials</span></h2>
  <svg class="abs" style="left:60px;top:282px" width="18" height="28" viewBox="0 0 18 28"><path d="M15 2L4 14l11 12" fill="none" stroke="#f15a22" stroke-width="4"/></svg>
  <svg class="abs" style="left:1130px;top:282px" width="18" height="28" viewBox="0 0 18 28"><path d="M3 2l11 12L3 26" fill="none" stroke="#f15a22" stroke-width="4"/></svg>
  <div class="t-card faded" style="left:114px;top:150px;width:310px;height:207px">
    <div class="q">&ldquo;</div><div class="avatar" role="img" aria-label="Client portrait"></div>
    <p>Lorem Ipsum is simply dummy text of the printing and typesetting industry. Lorem Ipsum has been the industry's standard dummy text ever since the 1500s, when an unknown printer took a galley of type and scrambled .</p>
  </div>
  <div class="t-card" style="left:450px;top:150px;width:310px;height:312px;box-shadow:0 2px 10px rgba(0,0,0,.08)">
    <div class="q">&ldquo;</div><div class="avatar" style="background:#9a8a80" role="img" aria-label="Client portrait"></div>
    <p>Lorem Ipsum is simply dummy text of the printing and typesetting industry. Lorem Ipsum has been the industry's standard dummy text ever since the 1500s, when an unknown printer took a galley of type and scrambled .</p>
    <p style="margin-top:14px">It was popularised in the 1960s with the release of Letraset sheets containing Lorem Ipsum passages.</p>
    <div class="name">MARA QUILL</div><div class="loc">USA</div>
  </div>
  <div class="t-card faded" style="left:785px;top:150px;width:312px;height:207px">
    <div class="q">&ldquo;</div><div class="avatar" role="img" aria-label="Client portrait"></div>
    <p>Lorem Ipsum is simply dummy text of the printing and typesetting industry. Lorem Ipsum has been the industry's standard dummy text ever since the 1500s, when an unknown printer took a galley of type and scrambled .</p>
  </div>
</section>

<footer class="footer">
  <div class="brand"><span class="mark"></span>CORVITHANE</div>
  <div class="f-tag">SCAFFOLDING RENTAL AND CONSTRUCTION COMPANY</div>
  <div class="f-call"><span class="accent">CALL US NOW :</span> 555 013 0000</div>
  <div class="socials" aria-label="Social links"><span></span><span></span><span></span></div>
  <div class="divider"></div>
  <h2>Contact <span class="accent">Us</span></h2>
  <div class="f-field" style="left:623px;top:146px;width:241px;height:33px">Your Name</div>
  <div class="f-field" style="left:872px;top:146px;width:241px;height:33px">Your Email</div>
  <div class="f-field" style="left:623px;top:189px;width:241px;height:33px">Phone No</div>
  <div class="f-field" style="left:872px;top:189px;width:241px;height:33px">Subject</div>
  <div class="f-field" style="left:623px;top:232px;width:490px;height:97px">Your Message</div>
  <div class="btn">Submit</div>
</footer>
<div class="copyright">© 2020 Corvithane All rights reserved</div>

</body>
</html>
```